Velmo BUSINESS CARD

Design an attention-grabbing business cards. Draw inspiration from the provided logo file. Please use the same font style as in the logo.
the back side of the card is for accent/decoration.

Contact Information for Business Card

PLEASE USE PROVIDED BUSINESS CARD SAMPLE

Other font styles liked:
• LUMETTE

Colors
EB3D1F
EC4F4E
F09395
F8D3D4
FCEDEE

Requirements
Must have
• RED, BLACK COLORS, SOLID BACK COLOR
Nice to have
• MAKE IT FANCY

```html
<!DOCTYPE html>
<html lang="en">
<head>
<meta charset="utf-8">
<title>Velmo Business Card</title>
<link rel="stylesheet" href="https://fonts.googleapis.com/css2?family=Audiowide&family=Lato:wght@400;700&display=swap">
<style>
  :root {
    --red: #e0202e;
    --red-deep: #c81a27;
    --black: #231f20;
    --black-soft: #2c2829;
    --white: #ffffff;
    --grey-text: #e6e6e6;
    --rule: #8a8a8a;
    --stage: #ecebea;
  }
  * { margin: 0; padding: 0; box-sizing: border-box; }
  html, body { width: 1200px; height: 801px; overflow: hidden; }
  body {
    background: var(--stage);
    font-family: "Lato", Arial, sans-serif;
    position: relative;
  }
  .card {
    position: absolute;
    top: 252px;
    width: 520px;
    height: 297px;
    border-radius: 16px;
    overflow: hidden;
    box-shadow: 0 10px 28px rgba(0,0,0,0.25);
  }
  .card-front { left: 50px; background: var(--red); }
  .card-back { left: 630px; background: var(--black); }

  .pattern-area {
    position: absolute; inset: 0;
    background: radial-gradient(circle at 50% 50%, var(--red) 0%, var(--red-deep) 100%);
    opacity: 0.55;
  }

  .brand { position: absolute; display: flex; align-items: center; }
  .brand-square { background: var(--white); flex: none; }
  .brand-name {
    font-family: "Audiowide", "Lato", sans-serif;
    color: var(--white);
    line-height: 1;
  }
  .brand-tagline {
    font-family: "Lato", Arial, sans-serif;
    color: var(--white);
    letter-spacing: 0.08em;
    white-space: nowrap;
  }

  .card-front .brand { left: 92px; top: 100px; }
  .card-front .brand-square { width: 78px; height: 78px; margin-right: 18px; }
  .card-front .brand-name { font-size: 74px; letter-spacing: 2px; }
  .card-front .brand-tagline { font-size: 13px; margin-top: 6px; margin-left: 4px; }

  .dragon-area {
    position: absolute; left: -40px; top: 40px; width: 320px; height: 300px;
    border-radius: 50%;
    background: radial-gradient(circle, var(--black-soft) 0%, var(--black) 70%);
  }
  .card-back .brand { right: 36px; top: 30px; }
  .card-back .brand-square { width: 40px; height: 40px; margin-right: 10px; }
  .card-back .brand-name { font-size: 38px; letter-spacing: 1px; }
  .card-back .brand-tagline { font-size: 7px; margin-top: 3px; margin-left: 2px; }

  .rule-main {
    position: absolute; left: 150px; right: 36px; top: 140px;
    height: 1px; background: var(--rule);
  }
  .person { position: absolute; left: 40px; top: 150px; }
  .person-name {
    font-family: "Audiowide", "Lato", sans-serif;
    color: var(--white); font-size: 25px; letter-spacing: 1px;
    white-space: nowrap;
  }
  .person-title { color: var(--red); font-size: 15px; margin-top: 2px; }
  .rule-person { width: 170px; height: 1px; background: var(--rule); margin: 10px 0 8px; }
  .contact-list { list-style: none; }
  .contact-list li {
    display: flex; align-items: center; gap: 8px;
    color: var(--grey-text); font-size: 13px; line-height: 19px;
    white-space: nowrap;
  }
  .contact-list svg { width: 10px; height: 10px; fill: var(--red); flex: none; }

  .address {
    position: absolute; right: 36px; top: 152px; text-align: right;
    color: var(--grey-text); font-size: 13px; line-height: 19px;
    white-space: nowrap;
  }
  .address .web { color: var(--red); }

  .edge-band { position: absolute; left: 0; right: 0; bottom: 0; height: 7px; display: flex; }
  .edge-band .red { flex: 7; background: var(--red); }
  .edge-band .white { flex: 3; background: var(--white); }
</style>
</head>
<body>
  <section class="card card-front">
    <div class="pattern-area" role="img" aria-label="Tone-on-tone red damask pattern"></div>
    <div class="brand">
      <div class="brand-square"></div>
      <div>
        <div class="brand-name">VELMO</div>
        <div class="brand-tagline">FREIGHT DONE RIGHT</div>
      </div>
    </div>
  </section>

  <section class="card card-back">
    <div class="dragon-area" role="img" aria-label="Faint large brand emblem decoration"></div>
    <div class="brand">
      <div class="brand-square"></div>
      <div>
        <div class="brand-name">VELMO</div>
        <div class="brand-tagline">FREIGHT DONE RIGHT</div>
      </div>
    </div>
    <div class="rule-main"></div>
    <div class="person">
      <div class="person-name">DANIEL ORTIZ</div>
      <div class="person-title">President</div>
      <div class="rule-person"></div>
      <ul class="contact-list">
        <li><svg viewBox="0 0 10 10"><path d="M2 0 L4 2 L3 3.5 Q4.5 6 6.5 7 L8 6 L10 8 L8.5 10 Q3 9 0 1.5 Z"/></svg>555-014-2231</li>
        <li><svg viewBox="0 0 10 10"><path d="M2.5 0 H7.5 V10 H2.5 Z M3.5 1 V8 H6.5 V1 Z"/></svg>555-018-7740</li>
        <li><svg viewBox="0 0 10 10"><path d="M0 1.5 H10 V8.5 H0 Z M0.8 2.2 L5 5.5 L9.2 2.2 Z"/></svg>DOrtiz@velmo-llc.com</li>
      </ul>
    </div>
    <div class="address">
      <div>1843 N. 250 East</div>
      <div>Brookdale, IN, 46999</div>
      <div class="web">www.Velmo-LLC.com</div>
    </div>
    <div class="edge-band"><span class="red"></span><span class="white"></span></div>
  </section>
</body>
</html>
```